FeedBack Solution Provider - Web Redesign

Lumora Website design request We are looking for a redesign for our website www.lumora-example.com 1 web page site +2, we are providing feedback collection solution through tablet devices and online iframes, sms, emails.. we want to optimize our website design to communicate our products values better (increase your customer satisfaction – get to know your customers – happy customers – increased business performance)Also to give visitors more insight to our different products (channels) layouts.A pricing section for minimum of 2 packages (SAAS) that include many features and hardware addons as a selection field. 3rd package clients to design their own packages through selection of components and addons no price needed in this feature (request quote).1 Web Page Sections will go as follows:1. Header2. Slider3. Why LuMora (points and values)4. Features 5. Packages (pricing based on SaaS and hardware as addon)6. Impact of using RaiBack7. Clients Testimonies8. Contact9. Footer +2 Web Pages Adding to additional web pages by copying the following sections with different content (will be hidden for the moment)1. Slider2. Features 3. Packages (pricing based on SaaS and hardware as addon)4. Impact of using RaiBack5. Clients TestimoniesHints: https://velkintor42.sitebuilder-example.com/lumora www.lumora-example.com

Target Market(s)

B2B

Industry/Entity Type

SaaS

Number of Pages Required

1 page

Font styles to use
Sans Serif

Colors

Designer to choose colors to be used in the design.

Requirements
Must have
• 1 Web Page Sections will go as follows:
• 1. Header
• 2. Slider
• 3. Why LuMora (points and values)
• 4. Features
• 5. Packages (pricing based on SaaS and hardware as addon)
• 6. Impact of using LuMora
• 7. Clients Testimonies
• 8. Contact
• 9. Footer
Nice to have
• +2 Web Pages Adding to additional web pages by copying the following sections with different content (will be hidden for the moment)
• 1. Slider
• 2. Features
• 3. Packages (pricing based on SaaS and hardware as addon)
• 4. Impact of using LuMora
• 5. Clients Testimonies

```html
<!DOCTYPE html>
<html lang="en">
<head>
<meta charset="utf-8">
<title>LuMora – Customer Feedback Solutions</title>
<link href="https://fonts.googleapis.com/css2?family=Lato:wght@300;400;700;900&display=swap" rel="stylesheet">
<style>
:root{
  --navy:#0c2340;
  --navy-mid:#163a63;
  --blue:#2f8fe0;
  --blue-light:#3d9bea;
  --orange:#f07f1d;
  --orange-red:#e0431a;
  --ink:#1d1d1d;
  --grey:#555;
  --pale:#f2f2f2;
  --white:#fff;
}
*{margin:0;padding:0;box-sizing:border-box}
html,body{width:1200px;height:3913px;overflow:hidden}
body{font-family:'Lato',sans-serif;color:var(--ink);background:var(--white);position:relative}
.abs{position:absolute}
.btn{position:absolute;display:flex;align-items:center;justify-content:center;font-weight:700;font-size:15px;letter-spacing:.5px;text-transform:uppercase;color:var(--white)}
.btn-orange{background:var(--orange)}
.btn-outline{border:2px solid var(--white)}

/* hero */
.hero-bg{left:0;top:0;width:1200px;height:790px;background:linear-gradient(110deg,#0b1f3a 0%,#163a63 55%,#1f5d96 100%);clip-path:polygon(0 0,100% 0,100% 64%,0 100%)}
.brand{left:140px;top:22px;display:flex;align-items:center;gap:14px;color:var(--white);font-size:32px;font-weight:700}
.brand-mark{width:58px;height:58px;border:3px solid var(--white);border-radius:50%}
.main-nav{left:418px;top:46px;display:flex;gap:30px;color:var(--white);font-size:17px;font-weight:700}
.lang{left:958px;top:38px;width:80px;height:38px;border:2px solid var(--white);color:var(--white);font-size:15px;font-weight:700;display:flex;align-items:center;justify-content:center;gap:8px}
.hero-title{left:140px;top:244px;width:470px;color:var(--white);font-size:33px;line-height:38px;font-weight:700}
.hero-text{left:140px;top:376px;width:430px;color:#c8d6e6;font-size:16px;line-height:23px}
.monitor{left:626px;top:130px;width:470px;height:535px}
.monitor-screen{left:0;top:0;width:470px;height:400px;background:#111;border-radius:14px;padding:18px}
.monitor-screen .screen-fill{width:100%;height:100%;background:linear-gradient(180deg,#f4f7fb,#dfe8f3)}
.monitor-chin{left:0;top:400px;width:470px;height:40px;background:#dcdde0;border-radius:0 0 14px 14px}
.monitor-stand{left:160px;top:440px;width:150px;height:95px;background:linear-gradient(180deg,#c9cacd,#eeeff1);clip-path:polygon(15% 0,85% 0,100% 100%,0 100%)}

/* why */
.section-title{left:0;width:1200px;text-align:center;font-size:35px;font-weight:700;color:var(--ink)}
.why-sub{left:330px;top:770px;width:540px;text-align:center;font-size:17px;line-height:22px;color:var(--grey)}
.why-card{width:216px;height:206px;border:2px solid #444;background:var(--white);text-align:center;padding:70px 16px 0}
.why-card h3{font-size:17px;line-height:20px;font-weight:900;margin-bottom:8px}
.why-card p{font-size:12.5px;line-height:16px;color:var(--grey)}
.why-icon{position:absolute;left:76px;top:-34px;width:64px;height:64px;border-radius:50%;background:var(--blue);border:4px solid var(--white);box-shadow:0 0 0 2px #444}

/* features */
.features-bg{left:0;top:1160px;width:1200px;height:515px;background:linear-gradient(120deg,#0b1f3a 0%,#123156 60%,#0e2848 100%);clip-path:polygon(0 12%,100% 0,100% 100%,0 89%)}
.features-accent{left:990px;top:1160px;width:210px;height:70px;background:var(--blue);clip-path:polygon(100% 0,100% 100%,0 100%)}
.features-title{top:1268px;color:var(--white)}
.feature{width:300px;color:var(--white)}
.feature-icon{position:absolute;left:0;top:0;width:86px;height:86px;border-radius:50%;background:var(--blue)}
.feature h3{margin-left:100px;font-size:21px;line-height:24px;font-weight:700;margin-bottom:10px}
.feature p{margin-left:100px;font-size:13.5px;line-height:17px;color:#d4deea}

/* packages */
.packages-bg{left:0;top:1640px;width:1200px;height:650px;background:var(--pale);clip-path:polygon(0 0,100% 6%,100% 100%,0 94%)}
.packages-title{top:1676px}
.plan{background:var(--white);text-align:center;box-shadow:0 2px 14px rgba(0,0,0,.14)}
.plan h4{font-size:17px;font-weight:700;letter-spacing:.5px}
.plan .price{font-size:46px;font-weight:400;margin:10px 0 18px}
.plan .price sup{font-size:24px;vertical-align:18px}
.plan .price small{font-size:24px}
.plan ul{list-style:none;margin:0 24px}
.plan li{font-size:14px;color:var(--grey);padding:11px 0;border-bottom:1px solid #ddd}
.plan .btn{position:relative;margin:22px auto 0;width:146px;height:36px;font-size:13px}
.plan-basic h4{color:var(--orange-red)}
.plan-premium h4{color:var(--orange-red)}
.plan-standard{background:linear-gradient(180deg,#0c2340 0%,#16457a 70%,#2f8fe0 100%);color:var(--white)}
.plan-standard li{color:#dfe9f5;border-color:rgba(255,255,255,.3)}

/* impact */
.impact-title{left:174px;top:2312px;font-size:35px;font-weight:700;color:var(--blue)}
.impact-text{left:176px;top:2378px;width:410px;font-size:14px;line-height:22px;color:#333}
.impact-text p{margin-bottom:8px}
.laptop{left:569px;top:2291px;width:540px;height:310px}
.laptop-lid{left:50px;top:0;width:440px;height:286px;background:#d8d9dc;border-radius:12px 12px 0 0;padding:14px}
.laptop-lid .screen-fill{width:100%;height:100%;background:linear-gradient(180deg,#ffffff,#f1f3f6)}
.laptop-base{left:0;top:286px;width:540px;height:20px;background:linear-gradient(180deg,#e6e7ea,#b7b8bc);border-radius:0 0 50% 50%/0 0 100% 100%}

/* testimonials */
.testi-bg{left:0;top:2646px;width:1200px;height:552px;background:var(--blue);clip-path:polygon(0 0,100% 10%,100% 100%,0 100%)}
.testi-title{top:2756px;color:var(--white)}
.avatar{left:556px;top:2822px;width:88px;height:88px;border-radius:50%;background:linear-gradient(160deg,#f0c9a8,#b9825c);border:3px solid var(--white)}
.quote{left:240px;top:2910px;width:720px;text-align:center;color:var(--white);font-size:19px;line-height:28px;font-weight:300}
.quote-mark{font-size:56px;font-weight:900;line-height:0;vertical-align:-20px}
.author{left:0;top:3030px;width:1200px;text-align:center;color:var(--white);font-size:19px;font-weight:700}
.dots{left:564px;top:3078px;display:flex;gap:8px}
.dots span{width:14px;height:14px;border:2px solid var(--white);border-radius:50%}
.dots span.on{background:var(--white)}

/* contact */
.contact-bg{left:0;top:3196px;width:1200px;height:548px;background:linear-gradient(120deg,#13243a,#1c3550 60%,#12263d)}
.contact-title{left:178px;top:3254px;font-size:37px;font-weight:700;color:var(--white)}
.info{left:180px;width:320px;color:var(--white)}
.info svg{position:absolute;left:0;top:4px}
.info h5{margin-left:58px;color:var(--blue-light);font-size:16px;font-weight:900;margin-bottom:4px}
.info p{margin-left:58px;font-size:16px;line-height:24px}
.field{left:532px;width:506px;height:48px;background:#0f1d2e;border:1px solid #3b4d63;color:#c9d3de;font-size:15px;padding:14px 16px}
.field-message{height:118px}

/* footer */
.foot-nav{left:0;top:3768px;width:1200px;display:flex;justify-content:center;gap:28px;font-size:17px;font-weight:700}
.copyright{left:0;top:3804px;width:1200px;text-align:center;font-size:13px;color:#333}
.socials{left:490px;top:3843px;display:flex;gap:14px}
.socials span{width:38px;height:38px;border-radius:50%;background:var(--blue)}
</style>
</head>
<body>

<!-- header + hero -->
<div class="abs hero-bg"></div>
<div class="abs brand"><span class="brand-mark"></span>LuMora</div>
<nav class="abs main-nav"><span>Lumora</span><span>Our Clients</span><span>Control Board</span><span>Advantages</span><span>More</span></nav>
<div class="abs lang">ENG
  <svg width="12" height="8" viewBox="0 0 12 8"><path d="M1 1l5 5 5-5" stroke="#fff" stroke-width="2" fill="none"/></svg>
</div>
<h1 class="abs hero-title">Learn about your Customers opinions, improve their experience with them</h1>
<p class="abs hero-text">Lorem ipsum dolor sit amet consectetuer adipiscing elit Nam cursus Morbi ut mi Nullam enim</p>
<div class="btn btn-outline" style="left:140px;top:455px;width:160px;height:44px">Learn more</div>
<div class="btn btn-orange" style="left:311px;top:455px;width:166px;height:44px">Get started</div>
<div class="abs monitor">
  <div class="abs monitor-screen"><div class="screen-fill" role="img" aria-label="Dashboard screen with donut charts and line graphs of customer feedback"></div></div>
  <div class="abs monitor-chin"></div>
  <div class="abs monitor-stand"></div>
</div>

<!-- why -->
<h2 class="abs section-title" style="top:712px">Why LuMora</h2>
<p class="abs why-sub">The most prominent features of the device and the application of LuMora to assess and measure customer satisfaction</p>
<div class="abs why-card" style="left:149px;top:874px"><span class="why-icon"></span><h3>Professional control panel</h3><p>Formulating surveys and monitoring performance through a number of graphical report</p></div>
<div class="abs why-card" style="left:378px;top:898px"><span class="why-icon"></span><h3>Various evaluation channels</h3><p>Via the LMR Pack system, to connect with the electronic platforms and the possibility of sending</p></div>
<div class="abs why-card" style="left:608px;top:874px"><span class="why-icon"></span><h3>Evaluation and comparison is not limited</h3><p>Create unlimited number of questionnaires and assign them to a branch, departme</p></div>
<div class="abs why-card" style="left:837px;top:898px"><span class="why-icon"></span><h3>Instantly follow your customers' opinions</h3><p>A direct update of the questionnaire results or evaluation questions of customers and beneficiaries</p></div>

<!-- features -->
<div class="abs features-bg" role="img" aria-label="Dark blue background photo of people working at a desk"></div>
<div class="abs features-accent"></div>
<h2 class="abs section-title features-title">Features</h2>
<div class="abs feature" style="left:143px;top:1356px"><span class="feature-icon"></span><h3>Customization and integrated control</h3><p>Support Arabic and English. Consistency with identity and the addition of the logo of the user</p></div>
<div class="abs feature" style="left:464px;top:1356px"><span class="feature-icon"></span><h3>Analysis</h3><p>It has been able to follow up on the extent of changing the level of satisfaction and evaluation of customer opinions with high accuracy</p></div>
<div class="abs feature" style="left:764px;top:1348px"><span class="feature-icon"></span><h3>Wide Range</h3><p>Create unlimited number of questionnaires and assign them to a branch, department or person as desired.</p></div>

<!-- packages -->
<div class="abs packages-bg"></div>
<h2 class="abs section-title packages-title">Our Packages</h2>
<div class="abs plan plan-basic" style="left:175px;top:1774px;width:271px;height:360px;padding-top:36px">
  <h4>BASIC</h4><div class="price"><sup>$</sup>30<small>.00</small></div>
  <ul><li>Morbi diam mauris</li><li>Aiverra in gravida eu</li><li>Mattis in ante Morbi</li><li>Eget arcu Morbi</li></ul>
  <div class="btn btn-orange">Click here</div>
</div>
<div class="abs plan plan-standard" style="left:446px;top:1748px;width:311px;height:412px;padding-top:62px">
  <h4>STANDARD</h4><div class="price"><sup>$</sup>45<small>.00</small></div>
  <ul><li>Morbi diam mauris</li><li>Aiverra in gravida eu</li><li>Mattis in ante Morbi</li><li>Eget arcu Morbi</li></ul>
  <div class="btn btn-orange">Click here</div>
</div>
<div class="abs plan plan-premium" style="left:757px;top:1774px;width:258px;height:360px;padding-top:36px">
  <h4>PREMIUM</h4><div class="price"><sup>$</sup>90<small>.00</small></div>
  <ul><li>Morbi diam mauris</li><li>Aiverra in gravida eu</li><li>Mattis in ante Morbi</li><li>Eget arcu Morbi</li></ul>
  <div class="btn btn-orange">Click here</div>
</div>

<!-- impact -->
<h2 class="abs impact-title">Impact of using LuMora</h2>
<div class="abs impact-text">
  <p>Through the LuMora Control Panel to evaluate and measure customer satisfaction, system users can view the results of assessments directly to allow administrators to track the level of services and performance</p>
  <p>Customer Satisfaction Assessment and Measurement is a simple and flexible application to measure the level of service</p>
</div>
<div class="btn btn-orange" style="left:180px;top:2557px;width:162px;height:47px;box-shadow:0 3px 8px rgba(0,0,0,.25)">Read more</div>
<div class="abs laptop">
  <div class="abs laptop-lid"><div class="screen-fill" role="img" aria-label="Survey screen with a row of four satisfaction rating faces"></div></div>
  <div class="abs laptop-base"></div>
</div>

<!-- testimonials -->
<div class="abs testi-bg"></div>
<h2 class="abs section-title testi-title">Client Testimonials</h2>
<div class="abs avatar" role="img" aria-label="Portrait photo of the client"></div>
<p class="abs quote"><span class="quote-mark">“</span> Pellentesque faucibus Ut accumsan ultricies elit Maecenas at justo id velit placerat molestie Donec dictum lectus non odio Cras a ante vitae enim iaculis aliquam Mauris nunc quam venenatis nec euismod sit <span class="quote-mark">”</span></p>
<div class="abs author">BY AUTHOR NAME</div>
<div class="abs dots"><span></span><span class="on"></span><span></span></div>

<!-- contact -->
<div class="abs contact-bg" role="img" aria-label="Dark background photo of an office"></div>
<h2 class="abs contact-title">Contact Us</h2>
<div class="abs info" style="top:3340px">
  <svg width="40" height="44" viewBox="0 0 40 44"><path d="M20 4a11 11 0 0 0-11 11c0 8 11 20 11 20s11-12 11-20A11 11 0 0 0 20 4z" fill="none" stroke="#fff" stroke-width="2"/><circle cx="20" cy="15" r="4" fill="none" stroke="#fff" stroke-width="2"/><path d="M6 34l-4 8h36l-4-8" fill="none" stroke="#fff" stroke-width="2"/></svg>
  <h5>ADDRESS</h5><p>4180 Cedarline Avenue, Northgate District, Velmora City</p>
</div>
<div class="abs info" style="top:3454px">
  <svg width="40" height="40" viewBox="0 0 40 40"><path d="M8 4l8 8-4 5c3 6 7 10 13 13l5-4 8 8-5 5C18 38 2 22 3 9z" fill="none" stroke="#fff" stroke-width="2"/></svg>
  <h5>PHONE NUMBER</h5><p>800555012 / 0550001234</p>
</div>
<div class="abs info" style="top:3538px">
  <svg width="40" height="32" viewBox="0 0 40 32"><rect x="2" y="4" width="36" height="24" fill="none" stroke="#fff" stroke-width="2"/><path d="M2 4l18 14L38 4M2 28l13-12M38 28L25 16" fill="none" stroke="#fff" stroke-width="2"/></svg>
  <h5>EMAIL US</h5><p>info@lumora-example.com</p>
</div>
<div class="abs field" style="top:3282px">Name</div>
<div class="abs field" style="top:3339px">Email address</div>
<div class="abs field" style="top:3396px">Phone</div>
<div class="abs field field-message" style="top:3453px">Message</div>
<div class="btn btn-orange" style="left:535px;top:3590px;width:164px;height:50px;font-size:17px">Submit</div>

<!-- footer -->
<nav class="abs foot-nav"><span>Lumora</span><span>Our Clients</span><span>Control Board</span><span>Advantages</span><span>More</span></nav>
<p class="abs copyright">© 2019 Company Name &nbsp;All right reserved</p>
<div class="abs socials"><span></span><span></span><span></span><span></span></div>

</body>
</html>
```